New custom software business needs a Wordpress site

We need a Wordpress site for a new company based out of Chicago called 'Vellora Consulting'. Using a mix of on and off-shore resources we build custom software solutions, mainly focusing on small to medium sized companies. We help our customers "aspire" to do great things.
We have a basic site up here: https://brindlewave.example/. We worked on the content for it but not the branding. For now, this houses all the pages (except for a Contact Us page we'll be adding soon) for the foreseeable future.
We also have a new logo (attached) that we'd like to base the styling/colors on.
Target Market(s)
Small to medium sized companies that require tech resources
Industry/Entity Type
Software
Nice to have
- Teamwork, tech, professional but not elitist

```html
<!DOCTYPE html>
<html lang="en">
<head>
<meta charset="utf-8">
<title>Vellora Consulting</title>
<link href="https://fonts.googleapis.com/css2?family=Audiowide&family=Exo+2:ital,wght@0,400;0,600;1,400&family=Open+Sans:wght@400;600&display=swap" rel="stylesheet">
<style>
:root{
  --blue:#0a4fb0;
  --blue-deep:#0748a6;
  --blue-mid:#5c97c9;
  --blue-light:#97bde6;
  --sky:#3a8bd4;
  --ink:#333a44;
  --grey-bg:#f4f4f4;
  --pale:#eef4fb;
  --white:#ffffff;
}
*{margin:0;padding:0;box-sizing:border-box}
html,body{width:1200px;height:4549px;overflow:hidden}
body{font-family:"Open Sans",sans-serif;color:var(--ink);background:var(--white);position:relative}
section,header,footer{position:absolute;left:0;width:1200px}
.display{font-family:"Audiowide",sans-serif;color:var(--blue);font-weight:400;letter-spacing:2px}
.brand{display:flex;align-items:center;gap:10px;font-family:"Exo 2",sans-serif;font-weight:600;color:var(--blue)}
.brand-dot{width:30px;height:30px;background:var(--blue);border-radius:50%}

/* header */
.site-header{top:0;height:92px;background:var(--white)}
.site-header .brand{position:absolute;left:152px;top:28px;font-size:20px}
.main-nav{position:absolute;left:552px;top:36px;display:flex;gap:34px;font-size:13px;letter-spacing:.5px}
.main-nav a{color:#222;text-decoration:none}
.main-nav a.active{color:var(--blue);border-bottom:2px solid var(--blue);padding-bottom:10px}

/* hero */
.hero{top:92px;height:609px;overflow:hidden}
.hero-photo{position:absolute;inset:0;background:linear-gradient(120deg,#d8d8d8,#8d9098 45%,#5c6470)}
.hero-panel{position:absolute;inset:0}
.hero-title{position:absolute;left:804px;top:200px;font-size:42px;line-height:60px;color:var(--white)}
.hero-text{position:absolute;left:806px;top:324px;width:330px;font-family:"Exo 2",sans-serif;font-weight:400;font-size:18px;line-height:23px;color:var(--white);letter-spacing:.5px}

/* about */
.about{top:701px;height:592px}
.about-visual{position:absolute;left:116px;top:122px;width:396px;height:342px;border-radius:8px;background:linear-gradient(150deg,#a9c9ef,#2a6cc8)}
.about h2{position:absolute;left:560px;top:98px;font-size:38px}
.about-copy{position:absolute;left:561px;top:158px;width:477px;font-size:14px;line-height:21px}
.about-copy p+p{margin-top:21px}
.btn{position:absolute;display:flex;align-items:center;gap:10px;height:48px;padding:0 22px 0 16px;border-radius:24px;background:var(--blue);color:var(--white);font-family:"Audiowide",sans-serif;font-size:13px;letter-spacing:2px;text-decoration:none}
.btn-dot{width:18px;height:18px;border:2px solid var(--white);border-radius:50%}
.about .btn{left:559px;top:417px}

/* services */
.services{top:1293px;height:673px;background:var(--grey-bg)}
.services h2{position:absolute;width:100%;text-align:center;top:92px;font-size:38px}
.service-card{position:absolute;top:183px;width:288px;height:362px;color:var(--white);text-align:center;padding:48px 26px 0}
.service-card svg{width:66px;height:66px;display:block;margin:0 auto 26px}
.service-card h3{font-family:"Exo 2",sans-serif;font-weight:600;font-size:20px;line-height:25px;min-height:50px;max-width:180px;margin:0 auto}
.service-card p{margin-top:28px;font-size:13px;line-height:19px}
.card-1{left:152px;background:var(--blue)}
.card-2{left:456px;background:var(--blue-mid)}
.card-3{left:763px;background:var(--blue-light)}

/* why */
.why{top:1966px;height:630px}
.why h2{position:absolute;left:152px;top:136px;font-size:38px}
.why-copy{position:absolute;left:154px;top:208px;width:440px;font-size:14px;line-height:21px}
.why-copy p+p{margin-top:21px}
.why .btn{left:153px;top:479px}
.why-photo{position:absolute;left:588px;top:65px;width:612px;height:501px;background:linear-gradient(100deg,#c7a880,#e8e3da 40%,#b8c2cc);clip-path:polygon(22% 0,100% 0,100% 100%,0 100%)}

/* partners */
.partners{top:2596px;height:353px;background:linear-gradient(180deg,#f3f8fc,#eaf3fb)}
.partners h2{position:absolute;width:100%;text-align:center;top:74px;font-size:30px;color:#1d2c3c}
.partner-badge{position:absolute;top:150px;width:110px;height:70px;background:#a9aeb6;border-radius:10px;opacity:.85}

/* testimonial */
.testimonial{top:2949px;height:530px;background:linear-gradient(90deg,#2a6cc4,var(--sky) 60%)}
.testimonial-photo{position:absolute;inset:0;background:radial-gradient(ellipse at 35% 40%,rgba(255,255,255,.12),transparent 60%)}
.quote-mark{position:absolute;width:100%;text-align:center;top:70px;font-family:Georgia,serif;font-size:140px;line-height:140px;color:var(--white);font-weight:700}
.quote-text{position:absolute;left:260px;width:680px;top:200px;text-align:center;font-family:"Exo 2",sans-serif;font-style:italic;font-size:25px;line-height:33px;color:var(--white)}
.author{position:absolute;left:457px;top:324px;display:flex;align-items:center;gap:14px;color:var(--white)}
.author-photo{width:92px;height:92px;border-radius:50%;border:3px solid var(--white);background:linear-gradient(160deg,#9b8a7a,#4a3f38)}
.author-name{font-family:"Exo 2",sans-serif;font-weight:600;font-size:17px}
.author-role{font-family:"Exo 2",sans-serif;font-size:14px}

/* blog */
.blog{top:3479px;height:671px}
.blog h2{position:absolute;width:100%;text-align:center;top:126px;font-size:38px}
.post{position:absolute;top:198px;width:245px;height:379px;background:var(--pale)}
.post-image{height:176px}
.post h3{margin:28px 26px 0 28px;font-family:"Exo 2",sans-serif;font-weight:600;font-size:19px;line-height:23px;color:var(--blue)}
.post p{margin:24px 28px 0;font-size:11px;line-height:17px;color:#333}
.post svg{display:block;margin:16px 0 0 30px}
.post-1{left:177px}.post-1 .post-image{background:linear-gradient(160deg,#2b3442,#a7aeb8)}
.post-2{left:477px}.post-2 .post-image{background:linear-gradient(160deg,#1d4f87,#6d8fb8)}
.post-3{left:772px}.post-3 .post-image{background:linear-gradient(160deg,#6d8f5a,#c79b52)}

/* footer */
.site-footer{top:4150px;height:399px;background:var(--blue-deep);color:var(--white)}
.site-footer .brand{position:absolute;left:155px;top:186px;color:var(--white);font-size:26px}
.site-footer .brand-dot{background:var(--white)}
.footer-col{position:absolute;top:82px}
.footer-col h4{font-family:"Audiowide",sans-serif;font-weight:400;font-size:21px;letter-spacing:1px;margin-bottom:18px}
.footer-col li{list-style:none;font-size:11px;line-height:25px}
.col-links{left:445px}.col-support{left:678px}.col-contact{left:902px}
.social{display:flex;gap:14px;margin-top:44px}
.social span{width:20px;height:20px;border-radius:50%;background:var(--white)}
.footer-rule{position:absolute;left:155px;right:155px;top:318px;border-top:1px solid rgba(255,255,255,.45)}
.copyright{position:absolute;width:100%;text-align:center;top:350px;font-size:11px}
</style>
</head>
<body>

<header class="site-header">
  <div class="brand"><span class="brand-dot"></span>Vellora Consulting</div>
  <nav class="main-nav">
    <a class="active" href="#">HOME</a>
    <a href="#">SERVICES</a>
    <a href="#">WHY VELLORA?</a>
    <a href="#">VELLORA LEADERSHIP</a>
  </nav>
</header>

<section class="hero">
  <div class="hero-photo" role="img" aria-label="Two colleagues reviewing work on a laptop in an office"></div>
  <svg class="hero-panel" width="1200" height="609" viewBox="0 0 1200 609">
    <polygon points="868,0 1200,0 1200,609 880,609 690,300" fill="#0a4fb0"/>
  </svg>
  <h1 class="display hero-title">VELLORA<br>CONSULTING</h1>
  <p class="hero-text">Software consulting company specializing in serving small to medium size businesses.</p>
</section>

<section class="about">
  <div class="about-visual" role="img" aria-label="Team photograph in blue tones"></div>
  <h2 class="display">ABOUT US</h2>
  <div class="about-copy">
    <p>Welcome to Vellora, a software consulting company specializing in serving small to medium size businesses. We understand the unique challenges and opportunities that these companies face, and we are dedicated to helping them succeed through innovative technology solutions.</p>
    <p>Our team of experienced professionals has a diverse range of skills and expertise, making us well-equipped to handle any project, big or small. We specialize in custom software development, working closely with our clients to understand their specific needs and build solutions that meet their requirements.</p>
  </div>
  <a class="btn" href="#"><span class="btn-dot"></span>READ MORE</a>
</section>

<section class="services">
  <h2 class="display">OUR SERVICES</h2>
  <div class="service-card card-1">
    <svg viewBox="0 0 66 66" fill="none" stroke="#fff" stroke-width="2"><rect x="6" y="6" width="24" height="24"/><rect x="36" y="6" width="24" height="24"/><rect x="6" y="36" width="24" height="24"/><rect x="36" y="36" width="24" height="24"/><circle cx="33" cy="18" r="4"/><circle cx="18" cy="33" r="4"/></svg>
    <h3>Custom Solution Delivery</h3>
    <p>Vellora offers a range of services focused on helping businesses and organizations deliver software solutions to their customers or users.</p>
  </div>
  <div class="service-card card-2">
    <svg viewBox="0 0 66 66" fill="none" stroke="#fff" stroke-width="2"><circle cx="33" cy="16" r="7"/><circle cx="16" cy="26" r="6"/><circle cx="50" cy="26" r="6"/><path d="M20 56v-12a13 13 0 0 1 26 0v12M4 56v-8a10 10 0 0 1 14-9M62 56v-8a10 10 0 0 0-14-9"/></svg>
    <h3>Staff Augmentation</h3>
    <p>Let Vellora help you supplement your existing software development teams with additional resources and expertise. We provided access to experienced</p>
  </div>
  <div class="service-card card-3">
    <svg viewBox="0 0 66 66" fill="none" stroke="#fff" stroke-width="2"><rect x="6" y="8" width="54" height="38" rx="2"/><path d="M24 56h18M33 46v10M27 22l-6 5 6 5M39 22l6 5-6 5M35 19l-4 16"/></svg>
    <h3>Custom Software Solutions</h3>
    <p>Vellora offers a range of services focused on helping businesses and organizations deliver software solutions to their customers or users.</p>
  </div>
</section>

<section class="why">
  <h2 class="display">WHY VELLORA?</h2>
  <div class="why-copy">
    <p>At Vellora, we are proud to have a team of seasoned IT professionals who understand what it takes to deliver a quality solution. Our team members have a wealth of experience and expertise in a variety of different areas, including software development, system integration, data migration, and software maintenance and support.</p>
    <p>We understand that delivering a high-quality software solution requires more than just technical expertise. It also requires a deep understanding of the needs and challenges of our clients, and the ability to work closely with them to develop a solution that meets their specific requirements.</p>
  </div>
  <a class="btn" href="#"><span class="btn-dot"></span>READ MORE</a>
  <div class="why-photo" role="img" aria-label="Team meeting around a conference table"></div>
</section>

<section class="partners">
  <h2 class="display">OUR TRUSTED PARTNERS...</h2>
  <div class="partner-badge" style="left:160px"></div>
  <div class="partner-badge" style="left:342px"></div>
  <div class="partner-badge" style="left:542px;width:70px;border-radius:50%"></div>
  <div class="partner-badge" style="left:692px"></div>
  <div class="partner-badge" style="left:866px;width:170px"></div>
</section>

<section class="testimonial">
  <div class="testimonial-photo" role="img" aria-label="Smiling colleagues in a blue-toned office scene"></div>
  <div class="quote-mark">&ldquo;</div>
  <p class="quote-text">&ldquo;Lorem ipsum dolor sit amet, consectetur adipiscing elit, sed do eiusmod tempor incididunt ut labore et dolore magna aliqua. Quis ipsum suspendisse ultrices gravida.&rdquo;</p>
  <div class="author">
    <div class="author-photo" role="img" aria-label="Portrait of the reviewer"></div>
    <div><div class="author-name">Marek Dovale</div><div class="author-role">VP Engineering</div></div>
  </div>
</section>

<section class="blog">
  <h2 class="display">LATEST BLOG POSTS</h2>
  <article class="post post-1">
    <div class="post-image" role="img" aria-label="Woman working on a laptop in a server room"></div>
    <h3>Lorem ipsum dolor sit amet, consectetur</h3>
    <p>Lorem ipsum dolor sit ametcon sectetur adipiscing elits lordo eiusmod tempor.</p>
    <svg width="32" height="14" viewBox="0 0 32 14" fill="none" stroke="#222" stroke-width="1.6"><path d="M0 7h30M24 1l6 6-6 6"/></svg>
  </article>
  <article class="post post-2">
    <div class="post-image" role="img" aria-label="Engineers reviewing a tablet in a data centre"></div>
    <h3>Lorem ipsum dolor sit amet, consectetur</h3>
    <p>Lorem ipsum dolor sit ametcon sectetur adipiscing elits lordo eiusmod tempor.</p>
    <svg width="32" height="14" viewBox="0 0 32 14" fill="none" stroke="#222" stroke-width="1.6"><path d="M0 7h30M24 1l6 6-6 6"/></svg>
  </article>
  <article class="post post-3">
    <div class="post-image" role="img" aria-label="Two colleagues talking in a bright office"></div>
    <h3>Lorem ipsum dolor sit amet, consectetur</h3>
    <p>Lorem ipsum dolor sit ametcon sectetur adipiscing elits lordo eiusmod tempor.</p>
    <svg width="32" height="14" viewBox="0 0 32 14" fill="none" stroke="#222" stroke-width="1.6"><path d="M0 7h30M24 1l6 6-6 6"/></svg>
  </article>
</section>

<footer class="site-footer">
  <div class="brand"><span class="brand-dot"></span>Vellora Consulting</div>
  <div class="footer-col col-links">
    <h4>LINKS</h4>
    <ul><li>Services</li><li>Custom Solution Delivery</li><li>Staff Augmentation</li><li>Why Vellora?</li><li>Vellora Leadership</li></ul>
  </div>
  <div class="footer-col col-support">
    <h4>SUPPORT</h4>
    <ul><li>Lorem ipsum dolor</li><li>Rit amet, consectetur</li><li>Adipiscing elit, sed do</li><li>Riusmod temporiunt</li><li>Qlabore et dolmagn</li></ul>
  </div>
  <div class="footer-col col-contact">
    <h4>CONTACT</h4>
    <ul><li>Comming Soon.</li></ul>
    <div class="social"><span></span><span></span><span></span><span></span></div>
  </div>
  <div class="footer-rule"></div>
  <p class="copyright">Copyright&copy; 2022 Vellora Consulting. All Rights Reserved.</p>
</footer>

</body>
</html>
```